Paws and Meadows is a dog walking service that offers home boarding and pet taxi

I am looking for a eye catching A5 leaflet/flyer design for my dog walking business Paws and Meadows.

The flyer must have my company logo on it (jpeg), a picture of my van (jpeg) and a picture of dogs playing (jpegs 1-5).

The fonts must be easy to read. I am not set on any colour scheme but do like the idea of having a natural background. IE. Green grass and blue sky or some forest setting with green trees. If you don't like this idea or its hard to work with don't worry I am open minded so be creative and do what you thinks best.

I'll provide quick feedback to designs that i like and so we can work together.

The flyers must contain the following:

60 minute group and individual walks
GPS Tracked Walks
Home Boarding
Pet Taxi
Puppy/Pet visits

Offer: 50% off first weeks dogs walks with this flyer.

As well as containing my contact info:

07915382046
www.paws-and-meadows.co.uk
paws-and-meadows@mailbrook.co.uk

Chatterbook, Chirpline and Snapgallery logos must be present as well.

Thanks and Good luck!

Target Market(s)

ANYONE WHO NEEDS THEIR DOG WALKED OR LOOKED AFTER WHEN THEY ARE ON HOLIDAY

Industry/Entity Type

Business

Contact Information for Business Card

THE BUSINESS CARD MUST DISPLAY THE LOGO THAT HAS BEEN UPLOADED IN A FILE. IT MUST LOOK SHARP AND PROFESSIONAL. CONTAIN ALL CONTACT INFO AND HAVE SERVICES OFFERED. SEE PROJECT DESCRIPTION FOR FLYER.

Font styles to use
Serif
Sans Serif

Requirements
Must have
• SEE PROJECT DESCRIPTION
Nice to have
• IT WOULD BE NICE TO HAVE PHOTOS OF MY VAN AND DOGS PLAYING. I HAVE UPLOADED SOME PICS OF VAN TO BE USED AND THERE ARE PICS OF DOGS PLAYING THAT COULD BE USED.

```html
<!DOCTYPE html>
<html lang="en">
<head>
<meta charset="utf-8">
<title>Paws and Meadows – Dog Walking Service</title>
<link rel="stylesheet" href="https://fonts.googleapis.com/css2?family=Alegreya+Sans:ital,wght@1,400&family=Anton&family=Varela+Round&family=Cutive+Mono&display=swap">
<style>
  :root {
    --ink: #1c1c1c;
    --brand-green: #2f6a2a;
    --contact-green: #1f5a1d;
    --sticker-orange: #f39a1f;
    --sticker-deep: #e07f10;
    --panel-top: #f4f4f4;
    --panel-bottom: #dcdcdc;
    --paper: #ffffff;
    --chatter: #3b66b0;
    --snap: #d6336c;
    --chirp: #36a6e6;
  }
  * { margin: 0; padding: 0; box-sizing: border-box; }
  html, body { width: 856px; height: 1200px; overflow: hidden; background: var(--paper); }
  .flyer { position: relative; width: 856px; height: 1200px; background: var(--paper); }

  .brand { position: absolute; top: 22px; left: 0; width: 856px; text-align: center; }
  .brand-mark { width: 200px; height: 200px; margin: 0 auto; border-radius: 50%;
    background: radial-gradient(circle at 50% 45%, #fbe3b9 0%, #f7b447 60%, #f29a1d 100%); }
  .brand-name { margin-top: 14px; font-family: "Varela Round", sans-serif; font-size: 40px;
    letter-spacing: 1px; color: var(--ink); line-height: 1; }
  .brand-tagline { display: flex; justify-content: center; align-items: center; gap: 6px; margin-top: 4px;
    font-family: "Varela Round", sans-serif; font-size: 13px; letter-spacing: 1.5px; color: var(--ink); }
  .brand-tagline::before, .brand-tagline::after { content: ""; width: 36px; height: 3px; background: var(--brand-green); }

  .panel { position: absolute; left: 18px; top: 296px; width: 820px; height: 886px; overflow: hidden;
    background: linear-gradient(180deg, var(--panel-top) 0%, #ececec 50%, var(--panel-bottom) 100%);
    box-shadow: 0 -6px 10px -4px rgba(0,0,0,0.35); }

  .social { position: absolute; top: 16px; left: 0; width: 820px; display: flex; justify-content: center;
    align-items: center; gap: 14px; font-family: "Varela Round", sans-serif; font-size: 15px; color: var(--ink); }
  .social-item { display: flex; align-items: center; gap: 6px; }
  .social-dot { width: 22px; height: 22px; border-radius: 50%; }
  .dot-chatter { background: var(--chatter); }
  .dot-snap { background: var(--snap); }
  .dot-chirp { background: var(--chirp); }

  .services { position: absolute; top: 80px; left: 0; width: 820px; list-style: none; text-align: center;
    font-family: "Alegreya Sans", sans-serif; font-style: italic; font-size: 40px; color: var(--ink); line-height: 47px; }
  .services li { display: flex; justify-content: center; align-items: center; gap: 8px; }
  .paw { width: 34px; height: 34px; flex: none; }

  .dogs-photo { position: absolute; left: 286px; top: 320px; width: 534px; height: 566px;
    background: linear-gradient(160deg, #c9a473 0%, #b58a55 30%, #2a221d 55%, #1c1816 75%, #3e6b2a 100%); }
  .meadow-grass { position: absolute; left: 0; top: 760px; width: 820px; height: 126px;
    background: linear-gradient(180deg, rgba(120,170,80,0) 0%, rgba(110,165,70,0.55) 45%, #5d9a3a 100%); }

  .offer-sticker { position: absolute; left: 30px; top: 330px; width: 264px; height: 264px; }
  .offer-text { position: absolute; left: 30px; top: 378px; width: 240px; text-align: center;
    font-family: "Anton", sans-serif; color: var(--ink); font-size: 90px; line-height: 82px; letter-spacing: -2px; }
  .offer-text sup { font-size: 44px; vertical-align: top; line-height: 1; }

  .contact-band { position: absolute; left: 0; top: 704px; width: 820px; height: 116px;
    background: linear-gradient(90deg, rgba(255,255,255,0.85) 0%, rgba(255,255,255,0.6) 55%, rgba(255,255,255,0) 80%); }
  .contacts { position: absolute; left: 22px; top: 708px; list-style: none;
    font-family: "Varela Round", sans-serif; font-size: 26px; color: var(--contact-green); line-height: 36px; }
  .contacts li { display: flex; align-items: center; gap: 14px; }
  .contact-icon { width: 36px; height: 26px; flex: none; }

  .offer-terms { position: absolute; left: 0; top: 836px; width: 820px; height: 36px; padding-left: 10px;
    background: linear-gradient(90deg, rgba(200,230,170,0.9) 0%, rgba(190,225,160,0.7) 60%, rgba(190,225,160,0) 100%);
    font-family: "Cutive Mono", monospace; font-size: 19px; line-height: 36px; color: var(--ink); }
</style>
</head>
<body>
<main class="flyer">
  <header class="brand">
    <div class="brand-mark" aria-hidden="true"></div>
    <div class="brand-name">PAWS AND MEADOWS</div>
    <div class="brand-tagline">DOG WALKING SERVICE</div>
  </header>

  <section class="panel">
    <div class="social">
      <span>Follow us on:</span>
      <span class="social-item"><span class="social-dot dot-chatter"></span>Chatterbook</span>
      <span class="social-item"><span class="social-dot dot-snap"></span>Snapgallery</span>
      <span class="social-item"><span class="social-dot dot-chirp"></span>Chirpline</span>
    </div>

    <div class="dogs-photo" role="img" aria-label="Photo of a golden dog and a black dog carrying a stick together through long grass"></div>
    <div class="meadow-grass" role="img" aria-label="Green meadow grass"></div>

    <ul class="services">
      <li><svg class="paw" viewBox="0 0 34 34"><g fill="#1c1c1c"><ellipse cx="17" cy="23" rx="8" ry="7"/><ellipse cx="8" cy="14" rx="3.5" ry="4.5"/><ellipse cx="14" cy="8" rx="3.5" ry="4.5"/><ellipse cx="21" cy="8" rx="3.5" ry="4.5"/><ellipse cx="27" cy="14" rx="3.5" ry="4.5"/></g></svg>60 minute group and individual walks</li>
      <li><svg class="paw" viewBox="0 0 34 34"><g fill="#1c1c1c"><ellipse cx="17" cy="23" rx="8" ry="7"/><ellipse cx="8" cy="14" rx="3.5" ry="4.5"/><ellipse cx="14" cy="8" rx="3.5" ry="4.5"/><ellipse cx="21" cy="8" rx="3.5" ry="4.5"/><ellipse cx="27" cy="14" rx="3.5" ry="4.5"/></g></svg>GPS Tracked Walks</li>
      <li><svg class="paw" viewBox="0 0 34 34"><g fill="#1c1c1c"><ellipse cx="17" cy="23" rx="8" ry="7"/><ellipse cx="8" cy="14" rx="3.5" ry="4.5"/><ellipse cx="14" cy="8" rx="3.5" ry="4.5"/><ellipse cx="21" cy="8" rx="3.5" ry="4.5"/><ellipse cx="27" cy="14" rx="3.5" ry="4.5"/></g></svg>Home Boarding</li>
      <li><svg class="paw" viewBox="0 0 34 34"><g fill="#1c1c1c"><ellipse cx="17" cy="23" rx="8" ry="7"/><ellipse cx="8" cy="14" rx="3.5" ry="4.5"/><ellipse cx="14" cy="8" rx="3.5" ry="4.5"/><ellipse cx="21" cy="8" rx="3.5" ry="4.5"/><ellipse cx="27" cy="14" rx="3.5" ry="4.5"/></g></svg>Pet Taxi</li>
      <li><svg class="paw" viewBox="0 0 34 34"><g fill="#1c1c1c"><ellipse cx="17" cy="23" rx="8" ry="7"/><ellipse cx="8" cy="14" rx="3.5" ry="4.5"/><ellipse cx="14" cy="8" rx="3.5" ry="4.5"/><ellipse cx="21" cy="8" rx="3.5" ry="4.5"/><ellipse cx="27" cy="14" rx="3.5" ry="4.5"/></g></svg>Puppy/Pet visits</li>
    </ul>

    <svg class="offer-sticker" viewBox="0 0 264 264" aria-hidden="true">
      <defs>
        <linearGradient id="peel" x1="0" y1="0" x2="1" y2="1">
          <stop offset="0" stop-color="#fff3a0"/>
          <stop offset="0.6" stop-color="#f2c21d"/>
          <stop offset="1" stop-color="#d89a0a"/>
        </linearGradient>
      </defs>
      <path d="M132 2 A130 130 0 1 0 262 132 L262 132 Q200 80 132 2 Z" fill="var(--sticker-orange)" stroke="var(--sticker-deep)" stroke-width="2"/>
      <path d="M132 2 Q200 80 262 132 Q230 150 200 110 Q160 60 132 2 Z" fill="url(#peel)"/>
    </svg>
    <div class="offer-text">50%<br>OFF<sup>*</sup></div>

    <div class="contact-band"></div>
    <ul class="contacts">
      <li><svg class="contact-icon" viewBox="0 0 36 26"><path d="M3 9 Q18 0 33 9 L30 13 L25 11 L24 7 Q18 5 12 7 L11 11 L6 13 Z" fill="#1f5a1d"/><path d="M9 14 L27 14 L31 24 L5 24 Z" fill="#1f5a1d"/><circle cx="18" cy="19" r="3" fill="#fff"/></svg>07915382046</li>
      <li><svg class="contact-icon" viewBox="0 0 36 26"><g fill="none" stroke="#1f5a1d" stroke-width="2"><circle cx="18" cy="13" r="11"/><ellipse cx="18" cy="13" rx="5" ry="11"/><line x1="7" y1="13" x2="29" y2="13"/><line x1="9" y1="7" x2="27" y2="7"/><line x1="9" y1="19" x2="27" y2="19"/></g></svg>www.paws-and-meadows.co.uk</li>
      <li><svg class="contact-icon" viewBox="0 0 36 26"><rect x="4" y="4" width="28" height="18" fill="#1f5a1d"/><path d="M4 4 L18 15 L32 4" fill="none" stroke="#fff" stroke-width="2"/></svg>paws-and-meadows@mailbrook.co.uk</li>
    </ul>

    <p class="offer-terms">*Offer: 50% off first weeks dogs walks with this flyer.</p>
  </section>
</main>
</body>
</html>
```